KRWB CERTIFICATES

We would like to redesign our swimming certificates. These are the certificates we give out to children in our swimming program every time they go up a level.

I have attached a copy of our current certificate to give you a general idea of what the layout etc.

This would be a 2 sided A4 full colour certificate template that we then individually print a child’s name and assessment details on to and present to them when they are assessed to move up a level

We are currently preparing to rebrand a number of areas of our program and these certificates should work to match the branding we are moving to. To help with this I have attached a copy of the template for our new website which should be operational within the next 4 to 6 weeks.

We are also about to release a new logo and it is attached for your use.

These certificates should also incorporate our new mascots & sea characters.

The KRWB boy & girl mascot should be used on all certificates. I have attached images of them in various positions for general use.

In all there will be 5 different certificates to suit the 5 sea characters we have to denote the 5 different stages within our program. The certificates should be designed to suit the general age of the children in that program:

Starfish – Toddler Program – 4 months to 3 years
Seahorse – Water Confidence Program – 3 to 6 years
Turtle – Learn-to-swim Program – 5 to 8 years
Fish – High end Learn-to-swim Program – 6 to 9 years
Dolphin – Squad Program – 7 to 12 years

The back of all certificates will be the same.

I would like the certificates to be bright, colourful, fun & age appropriate. I feel our current certificates are to busy and dated.

• White areas on the certificate so we can print the child's individual details onto the certificate.

'Teaching families to swim since 1994!'

Address & contact info as per our current certificate.

Website address & Loopvine logo.

'Congratulations' 'you have completed' Skills Achieved' as shown on our current certificate.

On the back of the certificate I would like to present and outline the KRWB boy & girl Mascots as well as the sea characters and link them to the program to which they represent.

```html
<!DOCTYPE html>
<html lang="en">
<head>
<meta charset="utf-8">
<title>KRWB Certificate – Front and Back</title>
<link rel="stylesheet" href="https://fonts.googleapis.com/css2?family=Open+Sans:wght@400;600;700&display=swap">
<style>
  :root {
    --pool-blue: #7fa3c8;
    --pool-light: #d7e3ef;
    --pool-right: #8db2d9;
    --navy: #2b3f8e;
    --sun-yellow: #f5dc3c;
    --aqua-line: #7cc8e4;
    --orange: #ea6a30;
    --ink: #1f1f1f;
    --slip-white: rgba(255, 255, 255, 0.72);
  }
  * { box-sizing: border-box; margin: 0; padding: 0; }
  html, body { width: 1200px; height: 842px; overflow: hidden; background: #ffffff; }
  body { font-family: "Open Sans", Arial, sans-serif; color: var(--ink); }

  .sheet { position: relative; width: 1200px; height: 842px; }
  .page { position: absolute; top: 0; height: 842px; overflow: hidden; }
  .page--front { left: 0; width: 601px; background: linear-gradient(90deg, var(--pool-light) 0%, var(--pool-blue) 22%, var(--pool-blue) 100%); }
  .page--back { left: 601px; width: 599px; background: linear-gradient(90deg, var(--pool-light) 0%, var(--pool-blue) 22%, var(--pool-blue) 100%); }
  .page > svg.backdrop { position: absolute; left: 0; top: 0; }

  .brand { position: absolute; display: flex; align-items: center; gap: 8px; font-weight: 700; font-size: 34px; letter-spacing: 1px; color: var(--navy); }
  .brand__dot { width: 20px; height: 20px; border-radius: 50%; background: var(--navy); }
  .page--front .brand { left: 52px; top: 52px; }
  .page--back .brand { left: 51px; top: 56px; }

  .contacts { position: absolute; top: 16px; font-size: 10px; line-height: 13.2px; color: var(--ink); white-space: nowrap; }
  .contacts strong { font-weight: 700; }
  .contacts p + p { margin-top: 13px; }
  .contacts--heights { left: 253px; }
  .contacts--marlow { left: 434px; }

  .headline { position: absolute; left: 45px; top: 774px; transform: rotate(-90deg); transform-origin: 0 0; font-size: 57px; line-height: 1; font-weight: 400; letter-spacing: 0.5px; color: var(--ink); white-space: nowrap; }

  .slip { position: absolute; background: var(--slip-white); box-shadow: 0 0 6px 3px rgba(255,255,255,0.45); }
  .slip--name { left: 189px; top: 214px; width: 357px; height: 57px; }
  .slip--program { left: 189px; top: 328px; width: 357px; height: 58px; }
  .slip--skills { left: 254px; top: 443px; width: 232px; height: 235px; }

  .label { position: absolute; font-size: 21px; color: var(--ink); text-align: center; }
  .label--completed { left: 189px; width: 357px; top: 287px; }
  .label--skills { left: 189px; width: 357px; top: 404px; font-size: 20px; }

  .art { position: absolute; border-radius: 50%; }
  .art--starfish-badge { left: 469px; top: 308px; width: 111px; height: 118px; background: radial-gradient(circle, #f6a1ab 0%, #ee8592 70%, rgba(238,133,146,0) 72%); }
  .art--mascots-front { left: 147px; top: 644px; width: 187px; height: 163px; border-radius: 40% 40% 20% 20%; background: radial-gradient(ellipse at 50% 55%, #e9592f 0%, #f0a060 55%, rgba(240,160,96,0) 72%); }
  .art--boy { left: 283px; top: 77px; width: 135px; height: 196px; border-radius: 45% 45% 30% 30%; background: radial-gradient(ellipse at 50% 50%, #e65a30 0%, #f2c8a4 55%, rgba(242,200,164,0) 72%); }
  .art--girl { left: 442px; top: 24px; width: 98px; height: 172px; border-radius: 45% 45% 30% 30%; background: radial-gradient(ellipse at 50% 50%, #e65a30 0%, #f6d08a 55%, rgba(246,208,138,0) 72%); }

  .tagline { position: absolute; left: 151px; top: 815px; font-size: 17.5px; line-height: 24px; color: var(--ink); white-space: nowrap; }
  .social { position: absolute; left: 477px; top: 772px; width: 102px; height: 30px; background: #ffffff; display: flex; align-items: center; gap: 6px; padding-left: 6px; font-size: 14px; font-weight: 600; color: var(--navy); }
  .social__mark { width: 18px; height: 18px; background: var(--navy); }
  .web { position: absolute; left: 477px; top: 813px; font-size: 11px; line-height: 16px; color: var(--ink); white-space: nowrap; }

  .intro { position: absolute; left: 113px; top: 192px; font-size: 17.5px; line-height: 24px; color: var(--ink); }

  .levels { position: absolute; left: 47px; top: 0; width: 330px; list-style: none; }
  .level { position: absolute; left: 0; width: 330px; height: 80px; }
  .level__slip { position: absolute; left: 51px; top: 16px; width: 272px; height: 48px; background: var(--slip-white); box-shadow: 0 0 6px 3px rgba(255,255,255,0.45); }
  .level__art { position: absolute; left: 0; top: 0; width: 78px; height: 80px; border-radius: 50%; }
  .level__name { position: absolute; left: 85px; top: 27px; font-size: 17.5px; line-height: 22px; color: var(--ink); white-space: nowrap; }
  .level__info { position: absolute; right: 14px; top: 24px; text-align: right; font-size: 8.5px; line-height: 13px; white-space: nowrap; }
  .level__info strong { display: block; font-size: 9.5px; font-weight: 700; }
  .level--starfish { top: 296px; }
  .level--seahorse { top: 398px; }
  .level--turtle { top: 500px; }
  .level--fish { top: 603px; }
  .level--dolphin { top: 708px; }
  .level--starfish .level__art { background: radial-gradient(circle, #f6a1ab 0%, #ee8592 62%, rgba(238,133,146,0) 72%); }
  .level--seahorse .level__art { background: radial-gradient(ellipse 40% 50%, #9a7bc0 0%, #7c5aa6 70%, rgba(124,90,166,0) 100%); }
  .level--turtle .level__art { background: radial-gradient(ellipse 42% 50%, #74b84c 0%, #4f9436 70%, rgba(79,148,54,0) 100%); }
  .level--fish .level__art { background: radial-gradient(ellipse 48% 50%, #f7c04a 0%, #ef9a2e 70%, rgba(239,154,46,0) 100%); }
  .level--dolphin .level__art { background: radial-gradient(ellipse 50% 46%, #8ad6ec 0%, #4eb7d8 70%, rgba(78,183,216,0) 100%); }

  .more-info { position: absolute; left: 113px; top: 803px; font-size: 10.5px; line-height: 16px; color: var(--ink); white-space: nowrap; }
</style>
</head>
<body>
<main class="sheet">

  <section class="page page--front" aria-label="Certificate front">
    <svg class="backdrop" width="601" height="842" viewBox="0 0 601 842" aria-hidden="true">
      <defs>
        <radialGradient id="header-glow" cx="0.3" cy="0.55" r="0.55">
          <stop offset="0" stop-color="#fdf3c4"/>
          <stop offset="0.45" stop-color="#f6b464"/>
          <stop offset="1" stop-color="#ea6a30"/>
        </radialGradient>
        <radialGradient id="footer-glow" cx="0.55" cy="0.35" r="0.6">
          <stop offset="0" stop-color="#fde7a4"/>
          <stop offset="0.5" stop-color="#f4a85a"/>
          <stop offset="1" stop-color="#ea6a30"/>
        </radialGradient>
      </defs>
      <path d="M0,0 H601 V112 C520,124 420,160 300,158 C180,156 80,132 0,140 Z" fill="url(#header-glow)"/>
      <path d="M0,146 C80,138 180,162 300,164 C420,166 520,130 601,118" fill="none" stroke="var(--sun-yellow)" stroke-width="3"/>
      <path d="M0,152 C80,144 180,168 300,170 C420,172 520,136 601,124" fill="none" stroke="var(--aqua-line)" stroke-width="3"/>
      <path d="M0,842 V838 C100,812 200,745 330,716 C440,696 530,694 601,692 V842 Z" fill="url(#footer-glow)"/>
      <path d="M0,832 C100,806 200,739 330,710 C440,690 530,688 601,686" fill="none" stroke="var(--sun-yellow)" stroke-width="3"/>
      <path d="M0,826 C100,800 200,733 330,704 C440,684 530,682 601,680" fill="none" stroke="var(--aqua-line)" stroke-width="2.5"/>
    </svg>

    <div class="brand"><span class="brand__dot"></span>KRWB</div>

    <div class="contacts contacts--heights">
      <p><strong>KRWB Hillcrest Heights</strong><br>Cnr Hill and Marlow Sts<br>Brookvale QLD 4999</p>
      <p>Ph: 07 5550 1201<br>Fax: 07 5550 1299<br>E: hhadmin@krwb.example.au</p>
    </div>
    <div class="contacts contacts--marlow">
      <p><strong>KRWB Marlow Aquatic Centre</strong><br>12 Bay St<br>Brookvale QLD 4999</p>
      <p>Ph: 07 5550 1244<br>Fax: 07 5550 1299<br>E: admin@krwb.example.au</p>
    </div>

    <h1 class="headline">CONGRATULATIONS</h1>

    <div class="slip slip--name"></div>
    <p class="label label--completed">you have completed</p>
    <div class="slip slip--program"></div>
    <div class="art art--starfish-badge" role="img" aria-label="Smiling pink starfish character"></div>
    <p class="label label--skills">SKILLS ACHIEVED</p>
    <div class="slip slip--skills"></div>

    <div class="art art--mascots-front" role="img" aria-label="Boy and girl mascots in graduation caps giving a high five"></div>

    <p class="tagline">Teaching families to swim since 1994!</p>
    <div class="social"><span class="social__mark"></span>Loopvine</div>
    <p class="web">www.krwb.example.au</p>
  </section>

  <section class="page page--back" aria-label="Certificate back">
    <svg class="backdrop" width="599" height="842" viewBox="0 0 599 842" aria-hidden="true">
      <path d="M564,0 C520,120 490,300 470,420 C450,560 400,720 344,842 H599 V0 Z" fill="var(--pool-right)"/>
      <path d="M564,0 C520,120 490,300 470,420 C450,560 400,720 344,842" fill="none" stroke="var(--navy)" stroke-width="9"/>
      <path d="M552,0 C508,120 478,300 458,420 C438,560 388,720 332,842" fill="none" stroke="var(--sun-yellow)" stroke-width="4"/>
    </svg>

    <div class="brand"><span class="brand__dot"></span>KRWB</div>

    <div class="art art--boy" role="img" aria-label="Boy mascot in graduation cap jumping"></div>
    <div class="art art--girl" role="img" aria-label="Girl mascot in graduation cap waving"></div>

    <p class="intro">You’ve graduated!<br>See where you’re<br>headed next...</p>

    <ul class="levels">
      <li class="level level--starfish">
        <div class="level__slip"></div>
        <div class="level__art" role="img" aria-label="Pink starfish character"></div>
        <span class="level__name">STARFISH</span>
        <span class="level__info">4 months - 3 years<strong>Toddler Program</strong></span>
      </li>
      <li class="level level--seahorse">
        <div class="level__slip"></div>
        <div class="level__art" role="img" aria-label="Purple seahorse character"></div>
        <span class="level__name">SEAHORSE</span>
        <span class="level__info">3 - 6 years<strong>Water Confidence Program</strong></span>
      </li>
      <li class="level level--turtle">
        <div class="level__slip"></div>
        <div class="level__art" role="img" aria-label="Green turtle character"></div>
        <span class="level__name">TURTLE</span>
        <span class="level__info">5 - 8 years<strong>Learn-to-Swim Program</strong></span>
      </li>
      <li class="level level--fish">
        <div class="level__slip"></div>
        <div class="level__art" role="img" aria-label="Orange fish character"></div>
        <span class="level__name">FISH</span>
        <span class="level__info">6 - 9 years<strong>High End Learn-to-Swim Program</strong></span>
      </li>
      <li class="level level--dolphin">
        <div class="level__slip"></div>
        <div class="level__art" role="img" aria-label="Light blue dolphin character"></div>
        <span class="level__name">DOLPHIN</span>
        <span class="level__info">9 - 12 years<strong>Squad Program</strong></span>
      </li>
    </ul>

    <p class="more-info">For more information visit www.krwb.example.au</p>
  </section>

</main>
</body>
</html>
```